Crumb Joy pastry business card design

I need a logo and a business card design for my baking business, "Crumb Joy". I daily bake French pastries from scratch using high quality ingredients and directly cater to local customers. My product is very authentic but sold at a casual setting . I'm looking for a simple, cute, stylish yet earthy design. Like this kind of feel:
http://clipvista.example/71946302
Target Market(s)
Metropolitan food conscious consumers in their 20-40s
Industry/Entity Type
Business
Requirements
Must have
- Soft pastel colors or other types of color schemes that would remind French pastries.
email: welovecrumbles@mailnest.example
chirp@bitemesf
www.crumbjoyla.example
Nice to have
Should not have
- pictures of pastries - sketches are ok.

```html
<!DOCTYPE html>
<html lang="en">
<head>
<meta charset="utf-8">
<title>Crumb Joy – Business Card</title>
<link rel="stylesheet" href="https://fonts.googleapis.com/css2?family=Libre+Baskerville&family=Arimo:wght@400&display=swap">
<style>
  :root {
    --page-bg: #efebe6;
    --card-white: #fdfcfc;
    --band-tan: #c8b7a5;
    --line-teal: #8fd1c9;
    --band-pink: #e9a3aa;
    --band-pink-light: #f3c7cb;
    --ink-mauve: #8a5a5e;
    --ring-blush: #f4e6e7;
    --logo-dot: #d9a0a7;
  }
  * { margin: 0; padding: 0; box-sizing: border-box; }
  html, body {
    width: 1200px;
    height: 1023px;
    overflow: hidden;
    background: var(--page-bg);
  }
  .business-card {
    position: absolute;
    left: 100px;
    top: 226px;
    width: 1000px;
    height: 572px;
    background: var(--card-white);
    box-shadow: 0 6px 24px rgba(80, 60, 40, 0.18);
    overflow: hidden;
  }
  .card-art {
    position: absolute;
    inset: 0;
    width: 100%;
    height: 100%;
  }
  .brand-lockup {
    position: absolute;
    left: 70px;
    top: 196px;
    display: flex;
    align-items: center;
    gap: 22px;
  }
  .brand-mark {
    width: 58px;
    height: 58px;
    border-radius: 50%;
    background: var(--logo-dot);
  }
  .brand-name {
    font-family: "Libre Baskerville", Georgia, serif;
    font-size: 52px;
    color: var(--ink-mauve);
    letter-spacing: 0.5px;
  }
  .contact-line {
    position: absolute;
    left: 60px;
    right: 60px;
    bottom: 72px;
    display: flex;
    justify-content: space-between;
    font-family: "Arimo", Arial, sans-serif;
    font-size: 22px;
    color: var(--ink-mauve);
  }
</style>
</head>
<body>
  <div class="business-card">
    <svg class="card-art" viewBox="0 0 1000 572" xmlns="http://www.w3.org/2000/svg">
      <defs>
        <radialGradient id="ringWash" cx="55%" cy="55%" r="60%">
          <stop offset="0%" stop-color="var(--ring-blush)" stop-opacity="0.9"/>
          <stop offset="100%" stop-color="var(--card-white)" stop-opacity="0"/>
        </radialGradient>
        <radialGradient id="swirlWash" cx="50%" cy="50%" r="50%">
          <stop offset="0%" stop-color="var(--band-pink-light)" stop-opacity="0.6"/>
          <stop offset="100%" stop-color="var(--band-pink-light)" stop-opacity="0"/>
        </radialGradient>
      </defs>
      <rect class="ring-pattern" x="0" y="60" width="1000" height="440" fill="url(#ringWash)" role="img" aria-label="Faint blush ring pattern across the card face"/>
      <path class="header-band" fill="var(--band-tan)"
        d="M0 0 H1000 V34 C860 34 760 42 620 70 C480 98 420 140 320 166 C220 190 110 176 0 190 Z"/>
      <path class="header-rule" fill="none" stroke="var(--line-teal)" stroke-width="3"
        d="M0 202 C110 188 220 202 322 178 C424 152 484 110 624 82 C764 54 860 46 1000 46"/>
      <ellipse class="swirl-ornament" cx="260" cy="320" rx="170" ry="60" fill="url(#swirlWash)" role="img" aria-label="Soft pink swirl ornament beneath the name"/>
      <rect class="footer-stripe" x="0" y="514" width="1000" height="14" fill="var(--band-pink-light)"/>
      <rect class="footer-band" x="0" y="528" width="1000" height="44" fill="var(--band-pink)"/>
    </svg>

    <div class="brand-lockup">
      <span class="brand-mark"></span>
      <span class="brand-name">Crumb Joy</span>
    </div>

    <div class="contact-line">
      <span class="contact-social">chirp@crumbjoyla</span>
      <span class="contact-web">www.crumbjoyla.example</span>
      <span class="contact-email">welovecrumbles@mailnest.example</span>
    </div>
  </div>
</body>
</html>
```